Online Spanish language company requires a book cover design.

We need a book cover design for a Spanish workbook that deals with what is often seen as a frightening grammar topic. The book is going to be called. 'Unlocking the Spanish Conditional Mood' with an extra sidebar which says: 'Take a breath and tackle the Conditional today!'

The idea of the book is to show students that it isn't that difficult and so the cover should reflect that. The key ideas are, safe/easy/structured/do-able.

The size of the book is 15.24 cm by 22.86cm

The authors are Warren Hale-Ortega and Beatrice Hale-Ortega

The book will have between 250 and 300 pages. We will have to confirm this once it is finished so that the spine can be adjusted accordingly.

Target Market(s)

English speaking market. Ages from 20 to 70 with a focus on 40 -60 age group.

Industry/Entity Type

It Company

Font styles to use
Sans Serif

Colors
fbee3e
ec1f27

Requirements
Must have
• Must have the feel of fun while maintaining an element of professionalism.
• On the back it must have a QR code (we will supply)
• Our BrightPath Spanish logo.
• A write up on the back about the contents and the authors.
Nice to have
• We are open to all ideas.
Should not have
• Let's not have flags or donkeys or flamenco. haha.

```html
<!DOCTYPE html>
<html lang="en">
<head>
<meta charset="utf-8">
<title>Unlocking the Spanish Conditional Mood – Book Cover</title>
<link rel="stylesheet" href="https://fonts.googleapis.com/css2?family=Oranienbaum&family=Open+Sans:wght@400;700&display=swap">
<style>
  :root {
    --sky-top: #e9f3f9;
    --sky-mid: #dbe9f2;
    --sky-low: #e4eef4;
    --title-blue: #1c4e77;
    --tagline-red: #ad2117;
    --example-light: #c3ccd3;
    --example-strong: #9fa9b2;
    --bowl-edge: #b9d3e2;
    --bowl-core: #eef6fa;
    --bowl-water: #9cc4da;
  }
  * { margin: 0; padding: 0; box-sizing: border-box; }
  html, body { width: 800px; height: 1200px; overflow: hidden; }
  body { background: var(--sky-top); }

  .cover {
    position: relative;
    width: 800px;
    height: 1200px;
    overflow: hidden;
    background:
      radial-gradient(ellipse 70% 12% at 30% 38%, rgba(255,255,255,0.75), transparent 70%),
      radial-gradient(ellipse 60% 10% at 80% 45%, rgba(255,255,255,0.6), transparent 70%),
      radial-gradient(ellipse 80% 14% at 50% 63%, rgba(255,255,255,0.55), transparent 70%),
      linear-gradient(180deg, var(--sky-top) 0%, var(--sky-mid) 45%, var(--sky-low) 100%);
  }

  .title {
    position: absolute;
    inset: 0;
    color: var(--title-blue);
    font-family: "Oranienbaum", "Times New Roman", serif;
    font-weight: 400;
  }
  .title span {
    position: absolute;
    left: 0;
    width: 800px;
    text-align: center;
    white-space: nowrap;
  }
  .title-lead {
    top: 52px;
    font-size: 86px;
    line-height: 100px;
  }
  .title-main {
    font-size: 116px;
    line-height: 130px;
    letter-spacing: 1px;
  }
  .title-main.line-one { top: 188px; }
  .title-main.line-two { top: 322px; }

  .tagline {
    position: absolute;
    top: 478px;
    left: 0;
    width: 800px;
    text-align: center;
    color: var(--tagline-red);
    font-family: "Open Sans", Arial, sans-serif;
    font-weight: 700;
    font-size: 29px;
    line-height: 40px;
    text-transform: uppercase;
  }

  .examples {
    position: absolute;
    inset: 0;
    font-family: "Open Sans", Arial, sans-serif;
    font-size: 21px;
    color: var(--example-light);
    white-space: nowrap;
    text-transform: uppercase;
  }
  .example { position: absolute; }
  .example b { color: var(--example-strong); font-weight: 700; }

  .fishbowl {
    position: absolute;
    left: 188px;
    top: 790px;
    width: 416px;
    height: 380px;
    border-radius: 48% 48% 50% 50% / 38% 38% 62% 62%;
    background:
      radial-gradient(ellipse 60% 45% at 50% 62%, var(--bowl-water), transparent 75%),
      radial-gradient(ellipse at 50% 50%, var(--bowl-core) 40%, var(--bowl-edge) 100%);
    opacity: 0.9;
  }
</style>
</head>
<body>
  <main class="cover">
    <h1 class="title">
      <span class="title-lead">Unlocking the Spanish</span>
      <span class="title-main line-one">CONDITIONAL</span>
      <span class="title-main line-two">MOOD</span>
    </h1>

    <p class="tagline">Take a breath and tackle<br>the Conditional today!</p>

    <div class="examples" aria-hidden="true">
      <span class="example" style="left:4px; top:690px;">yo <b>compraría</b> unos zapatos cómodos.</span>
      <span class="example" style="left:4px; top:735px;">dijo que <b>vendría</b>.</span>
      <span class="example" style="left:290px; top:735px;">el restaurante nos <b>serviría</b> la cena.</span>
      <span class="example" style="left:48px; top:782px;">ella <b>iría</b> a la fiesta.</span>
      <span class="example" style="left:430px; top:832px;">me dijo que me <b>llamaría</b>.</span>
      <span class="example" style="left:4px; top:905px;">pensé que <b>estarías</b> triste.</span>
      <span class="example" style="left:560px; top:905px;">sabía que <b>llegaría</b>.</span>
    </div>

    <div class="fishbowl" role="img" aria-label="Photograph of a round glass fishbowl with a goldfish leaping out of the water"></div>
  </main>
</body>
</html>
```